| ■お仕事内容 海外の高級ファッションブランドを販売するサイト用の無償修理保証のバナー製作をお願いいたします。 メンズ、レディースどちらも取り扱っているブランドのため、どちらでも使えるデザインが望ましいです。 ■バナーに記載する内容 「1年間無償修理保証」ということが伝わる文章を入れてください。 ※独自のサービスのため、「当店だけの・・・」など独自の付加価値サービスである文言を入れたいです。 ■重視する点 ・高級感のあるデザイン(ごちゃごちゃしていない、シンプルで目を引くもの) ・フラットデザインが基調になっているサイトにマッチするデザイン ・ファッション系のサイトに合うデザイン ・本物である安心感・信頼感のあるデザイン ■報酬 5,000円 ■応募条件 WEBサイトのバナー、アイコンなどの製作経験をお持ちの方 ご提案価格と実績のバランスを見てお仕事をお願いする方を選定させていただきます。 たくさんのご応募お待ちしております。 何卒宜しくお願いいたします。 |

```html
<!DOCTYPE html>
<html lang="ja">
<head>
<meta charset="UTF-8">
<title>1年間無償修理保証</title>
<link rel="stylesheet" href="https://fonts.googleapis.com/css2?family=Noto+Sans+JP:wght@700&family=Shippori+Mincho:wght@500&display=swap">
<style>
  :root {
    --gold: #b38d42;
    --gold-light: #d2b067;
    --brown-deep: #2f2111;
    --brown-mid: #45321a;
    --frame-line: #efe6d2;
    --headline: #f4ecda;
    --ribbon-red: #8e1c1c;
    --ribbon-fold: #5c0f0f;
    --ribbon-text: #f6eee0;
  }
  html, body {
    margin: 0;
    padding: 0;
    width: 1200px;
    height: 262px;
    overflow: hidden;
    background: #ffffff;
  }
  .banner {
    position: relative;
    width: 1200px;
    height: 262px;
    box-sizing: border-box;
    border: 8px solid var(--gold);
    overflow: hidden;
  }
  .banner__pattern {
    position: absolute;
    inset: 0;
    background:
      radial-gradient(ellipse at 50% 50%, var(--brown-mid) 0%, var(--brown-deep) 85%);
  }
  .banner__frame {
    position: absolute;
    left: 96px;
    top: 48px;
    width: 1064px;
    height: 152px;
    box-sizing: border-box;
    border: 2px solid var(--frame-line);
  }
  .banner__headline {
    position: absolute;
    left: 96px;
    top: 48px;
    width: 1064px;
    height: 152px;
    margin: 0;
    display: flex;
    align-items: center;
    justify-content: center;
    font-family: "Shippori Mincho", "Noto Serif JP", serif;
    font-weight: 500;
    font-size: 82px;
    letter-spacing: 26px;
    padding-left: 26px;
    box-sizing: border-box;
    color: var(--headline);
    line-height: 1;
  }
  .ribbon {
    position: absolute;
    left: -34px;
    top: 30px;
    width: 240px;
    height: 50px;
    transform: rotate(-22deg);
    transform-origin: center;
  }
  .ribbon__band {
    position: absolute;
    inset: 0;
    background: var(--ribbon-red);
    display: flex;
    align-items: center;
    justify-content: center;
    padding-left: 30px;
    box-sizing: border-box;
    font-family: "Noto Sans JP", sans-serif;
    font-weight: 700;
    font-size: 30px;
    letter-spacing: 2px;
    color: var(--ribbon-text);
    box-shadow: 0 3px 6px rgba(0,0,0,0.35);
  }
  .ribbon__fold {
    position: absolute;
    right: -14px;
    top: 0;
    width: 16px;
    height: 50px;
  }
</style>
</head>
<body>
  <div class="banner">
    <div class="banner__pattern" role="img" aria-label="Dark brown traditional lattice pattern background"></div>
    <div class="banner__frame"></div>
    <h1 class="banner__headline">1年間無償修理保証</h1>
    <div class="ribbon">
      <div class="ribbon__band">当店限定</div>
      <svg class="ribbon__fold" viewBox="0 0 16 50" aria-hidden="true">
        <polygon points="0,0 16,0 6,25 16,50 0,50" fill="var(--ribbon-fold)"/>
      </svg>
    </div>
  </div>
</body>
</html>
```